Modern Label for cleaning products for the brand Voralux

We need a label design for our line of cleaning products. The label should feature our logo and an image to identify the product's intended use. I've added our logo and an image for use. This only concerns the design of the label on the front of the bottle.

Label dimensions:
Label 1 (500ml bottle with spray): width 58mm x height 115mm
Label 2: (1L bottle): width 73mm x height 140mm
The design must be consistent for both bottles which you find in the pictures.

The bottles to be labeled are white. See the attachment for a photo of the bottles.

The photo must also appear on the label to identify the product's intended use.

Product information:
Brand: Voralux
Product: Sanitary Cleaner

This text must be placed on the label:
"Cleans, descales & freshens. followed with this text: "Ideal for quick and powerful cleaning. A ready-to-use product for everyday use."

- Mention the seperate USP's: Sanitary, Bathroom, Toilet, Wet areas

Appearance: This is a consumer product, but it must have a professional appearance. We would like to see a design that use the color blue from our logo.

Target Market(s)

Consumers who take care of their homes and want to maintain it the correct (professional) way

Font styles to use
Sans Serif

Colors
0054AA
0677BA
7BADD7
CADEEF
E8F1F8

Requirements
Must have
• USP's + use of image and logo + blend in 1 design
Nice to have
• Keep the color of the logo in the design
Should not have
• Comic sans

```html
<!DOCTYPE html>
<html lang="en">
<head>
<meta charset="utf-8">
<title>Voralux Sanitary Cleaner – front labels</title>
<link rel="stylesheet" href="https://fonts.googleapis.com/css2?family=Fira+Sans:ital,wght@0,500;0,600;0,700;1,700;1,800&family=Kaushan+Script&display=swap">
<style>
  :root {
    --blue-deep: #0054AA;
    --blue-mid: #0677BA;
    --blue-soft: #7BADD7;
    --blue-pale: #CADEEF;
    --blue-mist: #E8F1F8;
    --ink: #1c1c1e;
    --silver-light: #e6e9ec;
    --silver-dark: #9aa0a6;
    --page: #f1f2f4;
    --white: #ffffff;
  }
  * { box-sizing: border-box; margin: 0; padding: 0; }
  html, body { width: 1200px; height: 1013px; overflow: hidden; }
  body { background: var(--page); position: relative; font-family: "Fira Sans", sans-serif; }

  .label {
    position: absolute;
    overflow: hidden;
    background: var(--blue-mid);
    text-align: center;
    box-shadow: 0 2px 10px rgba(0,0,0,.12);
  }
  .label--500 { left: 150px; top: 217px; width: 373px; height: 739px; font-size: 12.73px; }
  .label--1000 { left: 640px; top: 56px; width: 469px; height: 900px; font-size: 16px; }

  .label__photo {
    position: absolute; inset: 0 0 50% 0;
    background: linear-gradient(180deg, #f3f4f5 0%, #e2e4e6 30%, #b9bbbd 62%, #9fa2a4 100%);
  }
  .label__shapes { position: absolute; inset: 0; width: 100%; height: 100%; }

  .brand { position: absolute; left: 0; right: 0; top: 7%; display: flex; flex-direction: column; align-items: center; }
  .brand__dot {
    width: 7.2em; height: 7.2em; border-radius: 50%;
    border: 0.9em solid var(--blue-mid); background: var(--white);
  }
  .brand__name {
    margin-top: 0.25em; font-weight: 700; font-size: 3.1em; line-height: 1;
    color: var(--ink); letter-spacing: -0.01em;
  }

  .usp { position: absolute; width: 16%; aspect-ratio: 1; transform: translate(-50%, -50%);
    border-radius: 50%; background: var(--blue-mist); border: 0.3em solid var(--blue-soft);
    display: flex; align-items: center; justify-content: center; }
  .usp svg { width: 62%; height: 62%; }
  .usp--tiles { left: 20.5%; top: 46%; }
  .usp--toilet { left: 44.7%; top: 46%; }
  .usp--sink { left: 67%; top: 41.7%; }
  .usp--bath { left: 89%; top: 37%; }

  .product { position: absolute; left: 0; right: 0; top: 51.5%; margin: 0; font-size: 1em; font-weight: normal; color: var(--white); }
  .product__name {
    display: block; font-family: "Kaushan Script", cursive; font-size: 7.6em; line-height: 0.85;
    transform: rotate(-6deg);
  }
  .product__type {
    display: block; font-weight: 800; font-style: italic; font-size: 5em; line-height: 0.95;
    transform: rotate(-5deg); margin: -0.02em 0 0 -0.3em; letter-spacing: 0.01em;
  }

  .claim {
    position: absolute; left: 0; right: 0; top: 73.8%;
    font-weight: 600; font-size: 2.75em; line-height: 1.08;
    background: linear-gradient(180deg, var(--silver-light) 0%, #b7bcc1 60%, #dfe2e5 100%);
    -webkit-background-clip: text; background-clip: text; color: transparent;
  }
  .description {
    position: absolute; left: 0; right: 0; top: 85.8%;
    font-weight: 500; font-size: 1.4em; line-height: 1.25; color: var(--white);
  }
  .volume {
    position: absolute; left: 0; width: 72%; bottom: 0.9%;
    font-weight: 700; font-size: 2.2em; line-height: 1; color: var(--blue-deep);
  }
  .label--500 .volume { font-size: 2.15em; width: 78%; bottom: 0.6%; }
</style>
</head>
<body>

<svg width="0" height="0" style="position:absolute">
  <defs>
    <linearGradient id="blueField" x1="0" y1="0" x2="0" y2="1">
      <stop offset="0" stop-color="#0677BA"/>
      <stop offset="1" stop-color="#0054AA"/>
    </linearGradient>
    <linearGradient id="silverBand" x1="0" y1="0" x2="1" y2="0">
      <stop offset="0" stop-color="#8f959b"/>
      <stop offset=".35" stop-color="#e9ebed"/>
      <stop offset=".7" stop-color="#b4b9be"/>
      <stop offset="1" stop-color="#d9dcdf"/>
    </linearGradient>
    <symbol id="icon-tiles" viewBox="0 0 40 40">
      <g fill="none" stroke="#0677BA" stroke-width="2">
        <rect x="4" y="4" width="32" height="32"/>
        <path d="M4 12h32M4 20h32M4 28h32M12 4v32M20 4v32M28 4v32"/>
      </g>
      <path d="M26 14l1.5 4 4 1.5-4 1.5-1.5 4-1.5-4-4-1.5 4-1.5z" fill="#0677BA"/>
    </symbol>
    <symbol id="icon-toilet" viewBox="0 0 40 40">
      <g fill="#0677BA">
        <rect x="10" y="4" width="10" height="14" rx="1.5"/>
        <path d="M8 18h24c0 6-4 9-8 10l1 8H13l1-8c-3-1-6-4-6-10z"/>
      </g>
      <path d="M30 6l1 2.5 2.5 1-2.5 1-1 2.5-1-2.5-2.5-1 2.5-1z" fill="#0677BA"/>
    </symbol>
    <symbol id="icon-sink" viewBox="0 0 40 40">
      <g fill="#0677BA">
        <path d="M18 4h4v8h-4z"/><path d="M14 6h12v2H14z"/>
        <path d="M6 16h28c0 5-5 8-10 8v12h-8V24c-5 0-10-3-10-8z"/>
      </g>
    </symbol>
    <symbol id="icon-bath" viewBox="0 0 40 40">
      <g fill="#0677BA">
        <path d="M10 20V8a4 4 0 0 1 8 0v1h-2V8a2 2 0 0 0-4 0v12z"/>
        <path d="M13 11h8l-4 3z"/>
        <path d="M4 20h32v3c0 5-4 9-9 9H13c-5 0-9-4-9-9z"/>
        <rect x="9" y="32" width="3" height="4"/><rect x="28" y="32" width="3" height="4"/>
      </g>
      <g fill="#0677BA"><circle cx="15" cy="16" r=".9"/><circle cx="18" cy="17" r=".9"/><circle cx="16" cy="18.5" r=".9"/></g>
    </symbol>
  </defs>
</svg>

<article class="label label--500">
  <div class="label__photo" role="img" aria-label="Photo of a bright modern bathroom with walk-in shower, vanity and bathtub"></div>
  <svg class="label__shapes" viewBox="0 0 100 100" preserveAspectRatio="none" aria-hidden="true">
    <path d="M0 44 C20 50 35 48 55 42 C72 37 85 36 100 35.5 V100 H0 Z" fill="url(#blueField)"/>
    <path d="M0 96 C25 94 45 92 65 93.5 C80 94.5 92 95.5 100 95.2 V100 H0 Z" fill="url(#silverBand)"/>
  </svg>
  <div class="brand"><span class="brand__dot"></span><span class="brand__name">voralux</span></div>
  <div class="usp usp--tiles" role="img" aria-label="Sanitary"><svg><use href="#icon-tiles"/></svg></div>
  <div class="usp usp--toilet" role="img" aria-label="Toilet"><svg><use href="#icon-toilet"/></svg></div>
  <div class="usp usp--sink" role="img" aria-label="Bathroom"><svg><use href="#icon-sink"/></svg></div>
  <div class="usp usp--bath" role="img" aria-label="Wet areas"><svg><use href="#icon-bath"/></svg></div>
  <h1 class="product"><span class="product__name">Sanitary</span><span class="product__type">CLEANER</span></h1>
  <p class="claim">Cleans, descales<br>&amp; freshens</p>
  <p class="description">Ideal for quick and powerful cleaning.<br>A ready-to-use product for everyday use.</p>
  <p class="volume">500ml</p>
</article>

<article class="label label--1000">
  <div class="label__photo" role="img" aria-label="Photo of a bright modern bathroom with walk-in shower, vanity and bathtub"></div>
  <svg class="label__shapes" viewBox="0 0 100 100" preserveAspectRatio="none" aria-hidden="true">
    <path d="M0 44 C20 50 35 48 55 42 C72 37 85 36 100 35.5 V100 H0 Z" fill="url(#blueField)"/>
    <path d="M0 97.5 C20 94 38 92.5 55 93 C75 93.6 90 95.5 100 95.8 V100 H0 Z" fill="url(#silverBand)"/>
  </svg>
  <div class="brand"><span class="brand__dot"></span><span class="brand__name">voralux</span></div>
  <div class="usp usp--tiles" role="img" aria-label="Sanitary"><svg><use href="#icon-tiles"/></svg></div>
  <div class="usp usp--toilet" role="img" aria-label="Toilet"><svg><use href="#icon-toilet"/></svg></div>
  <div class="usp usp--sink" role="img" aria-label="Bathroom"><svg><use href="#icon-sink"/></svg></div>
  <div class="usp usp--bath" role="img" aria-label="Wet areas"><svg><use href="#icon-bath"/></svg></div>
  <h2 class="product"><span class="product__name">Sanitary</span><span class="product__type">CLEANER</span></h2>
  <p class="claim">Cleans, descales<br>&amp; freshens</p>
  <p class="description">Ideal for quick and powerful cleaning.<br>A ready-to-use product for everyday use.</p>
  <p class="volume">1L</p>
</article>

</body>
</html>
```